Business Card Design Project

Hello,

We have just created our new COMPANY LOGO via Fenwick Loom and would not like to turn our attention to new Business Cards.

We are a printing company based in Singapore & Las Vegas. We specialize in blue-print printing for the Architectural, Engineering and Construction industries

The design should be simple, professional, clean and organized.

The Business Cards should "pop" when seen and will hopefully be something that makes you look twice.

We have two different Pan-tones that we use for our company, feel free to use them if you think they will work for your design?

Orange: PMS 021
Gray: PMS 431

I have attached our current logo for your use and reference which should obvious be on our business cards.

Considering we have two locations on different continents, we need business cards templates where the address details need to be interchangeable for each different location (total 2)

First one:
42 Mereton Road #03-11 to #03-15
Singapore 512847
Tel : +65 6483-2207
Fax : +65 6487-9042

Second one:
3218 W. Larkspur Blvd, Suite 204
Las Vegas, Nevada 89147
Tel : (702) 555-0143
Fax : (702) 555-0178

We would also like to list a few of our key services on the card. Here are a few examples to get you going.

Plan Printing & Plotting
Digital Colour Printing
Cadline Printing
Specialty Book Making
Scanning & Archiving
Collection & Delivey

This is the first time i have requested for business cards to be created so please let me know if you require any additional information.
Many Thanks,
Tomas
Updates

Reason: It took us longer than expected to finalize our Company Logo We look forward to receiving your designs.

Target Market(s)

Our Target Market is construction related people.
Construction
Architecture
Engineering

Industry/Entity Type

Printing

Font styles to use
Other font styles liked:
• Times New Roman

Colors
faa54b
ffffff

Requirements
Must have
• The business card must have our Company Logo (attached)
The font used must be Times New Roman
Should not have
• Playful images of print designs and/or logos

```html
<!DOCTYPE html>
<html lang="en">
<head>
<meta charset="utf-8">
<title>Arclen Plan Solutions – Business Card</title>
<link rel="stylesheet" href="https://fonts.googleapis.com/css2?family=Arimo:wght@700&family=Tinos:ital,wght@0,400;0,700;1,700&display=swap">
<style>
  :root {
    --backdrop: #3a4aa8;
    --card-dark: #0b0b0f;
    --card-light: #ffffff;
    --brand-orange: #f47a1f;
    --service-gray: #a9a9a9;
    --ink: #111111;
    --paper-white: #ffffff;
  }
  html, body {
    margin: 0;
    padding: 0;
    width: 1200px;
    height: 1000px;
    overflow: hidden;
    background: var(--backdrop);
  }
  .canvas {
    position: relative;
    width: 1200px;
    height: 1000px;
  }
  .card {
    position: absolute;
    top: 130px;
    width: 427px;
    height: 738px;
    border-radius: 18px;
    box-sizing: border-box;
  }
  .card--front {
    left: 147px;
    background: var(--card-dark);
    border: 1px solid #55585f;
  }
  .card--back {
    left: 626px;
    background: var(--card-light);
  }
  .brand-lockup {
    position: absolute;
    left: 0;
    right: 0;
    top: 335px;
    display: flex;
    justify-content: center;
    align-items: center;
    gap: 12px;
  }
  .brand-mark {
    width: 22px;
    height: 22px;
    background: var(--brand-orange);
    flex: none;
  }
  .brand-name {
    margin: 0;
    font-family: "Tinos", "Times New Roman", serif;
    font-weight: 700;
    font-size: 36px;
    line-height: 1.1;
    color: var(--brand-orange);
    white-space: nowrap;
  }
  .group-note {
    position: absolute;
    left: 0;
    right: 0;
    top: 686px;
    margin: 0;
    text-align: center;
    font-family: "Tinos", "Times New Roman", serif;
    font-style: italic;
    font-weight: 700;
    font-size: 19px;
    color: var(--paper-white);
  }
  .services {
    position: absolute;
    left: 34px;
    width: 356px;
    top: 40px;
    margin: 0;
    padding: 0;
    list-style: none;
    font-family: "Arimo", Arial, sans-serif;
    font-weight: 700;
    font-size: 29.5px;
    line-height: 35.6px;
    letter-spacing: 0.3px;
    color: var(--service-gray);
  }
  .services li {
    text-align: justify;
    text-align-last: justify;
    white-space: nowrap;
  }
  .services .spaced { letter-spacing: 5px; margin-right: -5px; }
  .address {
    position: absolute;
    left: 0;
    right: 0;
    top: 587px;
    margin: 0;
    text-align: center;
    font-family: "Tinos", "Times New Roman", serif;
    font-style: normal;
    font-size: 21px;
    line-height: 25.6px;
    color: var(--ink);
  }
</style>
</head>
<body>
  <div class="canvas">
    <section class="card card--front">
      <div class="brand-lockup">
        <span class="brand-mark"></span>
        <p class="brand-name">Arclen Plan Solutions</p>
      </div>
      <p class="group-note">A Member of the Arclen Group of Companies</p>
    </section>
    <section class="card card--back">
      <ul class="services">
        <li>Plan Printing &amp; Plotting</li>
        <li>Digital Colour Printing</li>
        <li class="spaced">Cadline Printing</li>
        <li>Specialty Book Making</li>
        <li>Scanning &amp; Archiving</li>
        <li>Collection &amp; Delivery</li>
      </ul>
      <address class="address">
        42 Mereton Road<br>
        #03-11 to #03-15<br>
        Singapore 512847<br>
        Tel : +65 6483-2207<br>
        Fax : +65 6487-9042
      </address>
    </section>
  </div>
</body>
</html>
```